Business Card design for Founder and CEO of new shoe company

I am looking for a business card design for my new shoe company called Strido.

I am launching the company this April. Strido shoes offers slip-on athletic and casual style shoes for men and women. The unique selling point of the brand is that all of our shoe exist without shoelaces. I have included a link to the website to offer additional information about the company, see product images, and gain inspiration for the design. You can use the store owner password "Strido" to access the website.

www.Strido-shop.example

Thanks,
Dean Porlow

Target Market(s)

Active Men and Women ages 16-45

Industry/Entity Type

Business

Contact Information for Business Card

Dean Porlow
Founder and CEO
www.Strido-shop.example
deanporlow@Strido-shop.example
888-730-1964 / 888-7STRIDO
Strido, LLC
2384 N Tarrow St
Chicago, IL 60614

Requirements
Must have
• Be able to quickly and easily tell that Strido is a shoe company from the business card

```html
<!DOCTYPE html>
<html lang="en">
<head>
<meta charset="utf-8">
<title>Strido — Business Card</title>
<link rel="stylesheet" href="https://fonts.googleapis.com/css2?family=Open+Sans:wght@400;600;700&display=swap">
<style>
  :root {
    --page-bg: #e9e7e4;
    --card-white: #fbfbfb;
    --card-black: #111112;
    --ink: #1b1b1b;
    --stripe-dark: #4a4a4c;
    --stripe-light: #b9b9bb;
    --name-white: #ffffff;
    --title-grey: #d4d4d4;
    --shoe-pink: #e0559a;
    --shoe-teal: #2cb7c9;
    --shoe-grey: #8f9397;
  }
  * { box-sizing: border-box; margin: 0; padding: 0; }
  html, body {
    width: 1200px; height: 716px; overflow: hidden;
    background: var(--page-bg);
    font-family: "Open Sans", Arial, sans-serif;
  }
  .canvas {
    width: 1200px; height: 716px;
    display: flex; align-items: center; justify-content: center; gap: 40px;
  }
  .card {
    position: relative;
    width: 520px; height: 297px;
    overflow: hidden;
    box-shadow: 0 6px 18px rgba(0,0,0,.18);
  }
  /* Back side */
  .card--back {
    background: var(--card-black);
    display: flex; align-items: center; justify-content: center;
  }
  .card--back .brand-name {
    color: #3a3a3c;
    font-size: 46px; font-weight: 400; letter-spacing: 1px;
  }
  /* Front side */
  .card--front { background: var(--card-white); }
  .brand-name--front {
    position: absolute; left: 30px; top: 22px;
    color: var(--ink);
    font-size: 40px; font-weight: 400; letter-spacing: 1px;
  }
  .contact-list {
    position: absolute; left: 30px; top: 90px;
    list-style: none;
    color: var(--ink);
    font-size: 11px; line-height: 16px;
  }
  .contact-list li { display: flex; align-items: center; gap: 6px; }
  .contact-list .icon { width: 10px; height: 10px; flex: none; fill: var(--ink); }
  .contact-list .no-icon { padding-left: 16px; }
  .product-photo {
    position: absolute; right: 18px; top: 78px;
    width: 150px; height: 112px;
    border-radius: 6px;
    background: linear-gradient(160deg, var(--shoe-pink) 0%, #f3c3dc 30%, var(--shoe-teal) 60%, var(--shoe-grey) 100%);
    opacity: .85;
  }
  .swoosh { position: absolute; left: 0; top: 0; width: 520px; height: 297px; }
  .holder {
    position: absolute; right: 40px; top: 222px;
    text-align: left;
  }
  .holder-name { color: var(--name-white); font-size: 18px; font-weight: 700; }
  .holder-title { color: var(--title-grey); font-size: 11px; font-weight: 400; margin-top: 2px; }
</style>
</head>
<body>
<main class="canvas">
  <section class="card card--back" aria-label="Card back">
    <span class="brand-name">Strido</span>
  </section>

  <section class="card card--front" aria-label="Card front">
    <svg class="swoosh" viewBox="0 0 520 297" aria-hidden="true">
      <path d="M0,150 C130,138 240,196 520,184" fill="none" stroke="var(--stripe-light)" stroke-width="3"/>
      <path d="M0,160 C130,150 240,205 520,194" fill="none" stroke="var(--stripe-dark)" stroke-width="7"/>
      <path d="M0,174 C130,164 240,220 520,208 L520,297 L0,297 Z" fill="var(--card-black)"/>
    </svg>

    <span class="brand-name brand-name--front">Strido</span>

    <ul class="contact-list">
      <li class="no-icon">2384 N Tarrow St Chicago, IL 60614</li>
      <li>
        <svg class="icon" viewBox="0 0 10 10"><path d="M2 0.5 L3.6 2.6 L2.7 3.6 C3.3 5 4.9 6.7 6.4 7.3 L7.4 6.4 L9.5 8 L8.4 9.5 C4.5 9.3 0.7 5.5 0.5 1.6 Z"/></svg>
        888-730-1964 / 888-7STRIDO
      </li>
      <li>
        <svg class="icon" viewBox="0 0 10 10"><path d="M0 2 H10 V8.5 H0 Z M0.8 2.6 L5 5.6 L9.2 2.6" fill="none" stroke="var(--ink)" stroke-width="1"/></svg>
        deanporlow@Strido-shop.example
      </li>
      <li>
        <svg class="icon" viewBox="0 0 10 10"><circle cx="5" cy="5" r="4.4" fill="none" stroke="var(--ink)" stroke-width="1"/><path d="M0.6 5 H9.4 M5 0.6 C2.6 3 2.6 7 5 9.4 M5 0.6 C7.4 3 7.4 7 5 9.4" fill="none" stroke="var(--ink)" stroke-width=".8"/></svg>
        www.Strido-shop.example
      </li>
    </ul>

    <div class="product-photo" role="img" aria-label="Photo of a row of colourful laceless athletic shoes"></div>

    <div class="holder">
      <p class="holder-name">Dean Porlow</p>
      <p class="holder-title">Founder and CEO</p>
    </div>
  </section>
</main>
</body>
</html>
```